Up to the Challenge - PPT Template with Splash Slide

We are looking for a PPT template that has 4 slides.
1. Splash slide (Creative, fun, no content, a visual representation of the theme)
2. Section header slide
3. Content Slide
4. Content Slide, another design option
The theme is 'UP to the Challenge'. The design should reflect this theme.
The colors should be in Purple (#864B99), Blue (#0A80C2), and Green (#52B054).

```html
<!DOCTYPE html>
<html lang="en">
<head>
<meta charset="utf-8">
<title>Up to the Challenge – Presentation Template</title>
<link rel="stylesheet" href="https://fonts.googleapis.com/css2?family=Anton&family=Open+Sans:wght@400;700;800&display=swap">
<style>
  :root {
    --purple: #864B99;
    --blue: #0A80C2;
    --green: #52B054;
    --ink: #111111;
    --paper: #ffffff;
    --muted: #333333;
  }
  * { box-sizing: border-box; margin: 0; padding: 0; }
  html, body { width: 1200px; height: 2772px; overflow: hidden; background: var(--paper); }
  body { position: relative; font-family: 'Open Sans', Arial, sans-serif; color: var(--ink); }

  .slide {
    position: absolute; left: 72px; width: 1056px; height: 594px;
    overflow: hidden; background: var(--paper);
    box-shadow: 0 2px 10px rgba(0,0,0,0.25);
  }
  .slide--splash { top: 99px; }
  .slide--section { top: 759px; }
  .slide--content-one { top: 1419px; }
  .slide--content-two { top: 2079px; }

  .photo { position: absolute; }

  /* Splash */
  .splash-photo {
    inset: 0;
    background:
      linear-gradient(90deg, #ffffff 0%, #fdf3f3 28%, rgba(255,255,255,0) 55%),
      linear-gradient(180deg, #3b3f5c 0%, #b46a7a 35%, #f08a5d 58%, #d9aab0 80%, #ececf2 100%);
  }
  .splash-rock {
    right: 0; top: 0; width: 330px; height: 100%;
    background: linear-gradient(100deg, #2a2428 0%, #14171b 60%, #0c0e10 100%);
    clip-path: polygon(35% 0, 100% 0, 100% 100%, 0 100%, 18% 60%, 28% 30%);
  }
  .splash-title {
    position: absolute; left: 36px; top: 130px;
    font-family: 'Anton', Impact, sans-serif; font-size: 128px; line-height: 0.98;
    text-transform: uppercase; letter-spacing: 1px;
    background: linear-gradient(120deg, #1a1a2a 0%, var(--purple) 30%, #e0465d 55%, #f2a04a 72%, var(--blue) 100%);
    -webkit-background-clip: text; background-clip: text; color: transparent;
  }

  /* Section header */
  .maze-photo {
    inset: 0;
    background:
      radial-gradient(ellipse at 50% 40%, #7d8790 0%, #3d454c 35%, #15191d 75%, #07090b 100%);
  }
  .section-title {
    position: absolute; left: 0; right: 0; top: 180px; text-align: center;
    font-family: 'Anton', Impact, sans-serif; font-size: 96px; letter-spacing: 2px;
    color: var(--blue); text-transform: uppercase;
    text-shadow: 0 4px 0 #064e78, 0 8px 14px rgba(0,0,0,0.6);
  }

  /* Content slide 1 */
  .content-title {
    position: absolute; left: 42px; top: 30px;
    font-family: 'Open Sans', Arial, sans-serif; font-weight: 800; font-size: 54px;
    text-transform: uppercase; color: var(--ink); letter-spacing: -0.5px;
  }
  .intro {
    position: absolute; left: 44px; top: 118px; width: 470px;
    font-size: 15px; line-height: 1.35; color: var(--muted);
  }
  .intro b, .point b, .column b { color: var(--ink); font-weight: 700; }
  .points-band {
    position: absolute; left: 0; top: 196px; width: 640px; height: 306px;
    background: var(--blue);
  }
  .points { position: absolute; left: 44px; top: 232px; list-style: none; width: 440px; }
  .point {
    display: flex; align-items: center; gap: 16px; margin-bottom: 22px;
    font-size: 14px; line-height: 1.3; color: #ffffff;
  }
  .point b { color: #ffffff; }
  .point-number {
    flex: 0 0 36px; height: 36px; border-radius: 50%;
    background: #ffffff; color: var(--blue);
    font-weight: 800; font-size: 13px; display: flex; align-items: center; justify-content: center;
  }
  .boulder-art { position: absolute; right: 0; top: 0; }

  /* Content slide 2 */
  .ladder-photo {
    left: 0; top: 0; width: 300px; height: 100%;
    background: linear-gradient(180deg, #d9d9d9 0%, #9a9a9a 45%, #5d5d5d 100%);
  }
  .label-band {
    position: absolute; left: 0; top: 382px; width: 368px; height: 116px;
    background: var(--purple); padding: 10px 0 0 30px;
    font-family: 'Open Sans', Arial, sans-serif; font-weight: 800; font-size: 44px; line-height: 1.0;
    color: #ffffff; text-transform: uppercase;
  }
  .columns {
    position: absolute; left: 410px; top: 34px; width: 600px;
    display: grid; grid-template-columns: 1fr 1fr; column-gap: 60px; row-gap: 58px;
  }
  .column { font-size: 14px; line-height: 1.32; color: var(--muted); }
  .column svg { display: block; margin: 0 0 14px 8px; }
  .column b { display: block; }
</style>
</head>
<body>

<section class="slide slide--splash">
  <div class="photo splash-photo" role="img" aria-label="Climber scaling a cliff against a sunset sky"></div>
  <div class="photo splash-rock" role="img" aria-label="Dark rock face with a climber"></div>
  <h1 class="splash-title">Up<br>to the<br>challenge</h1>
</section>

<section class="slide slide--section">
  <div class="photo maze-photo" role="img" aria-label="Person standing at the entrance of a giant stone maze"></div>
  <h2 class="section-title">Section Header</h2>
</section>

<section class="slide slide--content-one">
  <h2 class="content-title">Content Slide 1</h2>
  <p class="intro"><b>Lorem Ipsum</b> is simply dummy text of the printing and typesetting industry. Lorem Ipsum has been the industry's standard dummy text ever since the 1500s.</p>
  <div class="points-band"></div>
  <ol class="points">
    <li class="point"><span class="point-number">01</span><span><b>Lorem Ipsum</b> is simply dummy text of the printing and typesetting industry.</span></li>
    <li class="point"><span class="point-number">02</span><span><b>Lorem Ipsum</b> is simply dummy text of the printing and typesetting industry.</span></li>
    <li class="point"><span class="point-number">03</span><span><b>Lorem Ipsum</b> is simply dummy text of the printing and typesetting industry.</span></li>
    <li class="point"><span class="point-number">04</span><span><b>Lorem Ipsum</b> is simply dummy text of the printing and typesetting industry.</span></li>
  </ol>
  <svg class="boulder-art" width="500" height="594" viewBox="0 0 500 594" role="img" aria-label="Person pushing a huge boulder uphill at sunset">
    <defs>
      <linearGradient id="sunset" x1="0" y1="0" x2="0" y2="1">
        <stop offset="0" stop-color="#6e7fa0"/>
        <stop offset="0.45" stop-color="#e9a35a"/>
        <stop offset="0.7" stop-color="#b8652f"/>
        <stop offset="1" stop-color="#3a2a22"/>
      </linearGradient>
    </defs>
    <path d="M120 0 H500 V594 H110 C 40 520, 20 400, 30 290 C 40 170, 70 70, 120 0 Z" fill="url(#sunset)"/>
  </svg>
</section>

<section class="slide slide--content-two">
  <div class="photo ladder-photo" role="img" aria-label="Man on a tall ladder looking through binoculars into a grey sky"></div>
  <h2 class="label-band">Content<br>Slide 2</h2>
  <div class="columns">
    <div class="column">
      <svg width="64" height="56" viewBox="0 0 64 56" aria-hidden="true">
        <circle cx="32" cy="28" r="26" fill="none" stroke="var(--blue)" stroke-width="3"/>
        <path d="M14 30 L24 22 L32 26 L40 22 L50 30 L38 40 L28 38 Z" fill="var(--blue)"/>
      </svg>
      <b>Column 1</b>
      Lorem Ipsum is simply dummy text of the printing and typesetting industry. Lorem Ipsum has been the industry's standard dummy text ever since the 1500s.
    </div>
    <div class="column">
      <svg width="64" height="56" viewBox="0 0 64 56" aria-hidden="true">
        <circle cx="32" cy="12" r="7" fill="var(--blue)"/>
        <circle cx="14" cy="38" r="6" fill="var(--blue)"/>
        <circle cx="50" cy="38" r="6" fill="var(--blue)"/>
        <path d="M22 30 A10 10 0 0 1 42 30 Z" fill="var(--blue)"/>
        <path d="M5 56 A9 9 0 0 1 23 56 Z M41 56 A9 9 0 0 1 59 56 Z" fill="var(--blue)"/>
      </svg>
      <b>Column 2</b>
      Lorem Ipsum is simply dummy text of the printing and typesetting industry. Lorem Ipsum has been the industry's standard dummy text ever since the 1500s.
    </div>
    <div class="column">
      <svg width="64" height="56" viewBox="0 0 64 56" aria-hidden="true">
        <path d="M20 56 V44 C8 38 8 14 28 8 C46 4 56 18 52 30 L56 38 H50 V48 H40 V56 Z" fill="var(--blue)"/>
        <circle cx="32" cy="26" r="7" fill="#ffffff"/>
        <circle cx="32" cy="26" r="3" fill="var(--blue)"/>
      </svg>
      <b>Column 3</b>
      Lorem Ipsum is simply dummy text of the printing and typesetting industry. Lorem Ipsum has been the industry's standard dummy text ever since the 1500s.
    </div>
    <div class="column">
      <svg width="64" height="56" viewBox="0 0 64 56" aria-hidden="true">
        <circle cx="32" cy="14" r="9" fill="var(--blue)"/>
        <circle cx="12" cy="20" r="7" fill="var(--blue)"/>
        <circle cx="52" cy="20" r="7" fill="var(--blue)"/>
        <path d="M18 56 A14 16 0 0 1 46 56 Z" fill="var(--blue)"/>
        <path d="M0 52 A12 14 0 0 1 20 36 L16 52 Z M64 52 A12 14 0 0 0 44 36 L48 52 Z" fill="var(--blue)"/>
      </svg>
      <b>Column 4</b>
      Lorem Ipsum is simply dummy text of the printing and typesetting industry. Lorem Ipsum has been the industry's standard dummy text ever since the 1500s.
    </div>
  </div>
</section>

</body>
</html>
```